New Website Footer for a Supercar dealership.

I'm looking to get a newly designed footer created for our website www.velmorcarhouse.com - one version for Desktop and 1 trimmed down version for mobile. We have one in place at the moment but I want to start it from scratch and create something far better. I know what I want to include and I have a rough design to work from which I have included in the uploaded files and I am just looking for someone to give it a high end luxury design.

If you see the sketch I've done - it must include the following links
- CURRENT STOCK
- SELL YOUR CAR
- PREVIOUSLY SOLD
Ideally use the same font that we have on our website in the top navigation

Secondary Links (in lower case)
- Delivery & Shipping
- Privacy Policy
- Modern Slavery Statement
- Luxury Cars
- Contact Us

I want also want to include
- Opening Hours
- Widget for Ratewell
- Widget for Praisly Reviews
- 4 images for awards we have won (I have included in uploaded files)
- Mailing List Sign Up
- Our company logo and address
- Quorin Finance logo (partner)
- Cookie Policy and Site Map links.
- Social Media icons

You do not have to stick to the layout of my design - feel free to change it about. I am open to colour but it needs to stay subtle and ideally working within Greyscale.

I am looking to have a black background but has a textured element to it. I was thinking along the lines of carbon fibre effect or even better would be a "Forged carbon fibre" effect in the background - I have included a screenshot of what ford carbon fibre looks like.

Target Market(s)

Luxury high end buyers

Industry/Entity Type

Automotive

Number of Pages Required

1 page

Font styles to use
Serif
Sans Serif

Colors

Designer to choose only greyscale colors for use in the design.

Requirements
Must have
• 1 Version for Desktop
1 Version for Mobile

```html
<!DOCTYPE html>
<html lang="en">
<head>
<meta charset="utf-8">
<title>Velmor Car House — Footer</title>
<link href="https://fonts.googleapis.com/css2?family=Mulish:wght@400;600;700&display=swap" rel="stylesheet">
<style>
  :root{
    --ink:#ffffff;
    --ink-soft:#e6e6e6;
    --ink-muted:#a9a9a9;
    --bg-deep:#101010;
    --bg-mid:#262626;
    --band:#000000;
    --button:#2f2f2f;
    --badge-light:#f2f2f2;
    --badge-dark:#1a1a1a;
  }
  *{box-sizing:border-box;margin:0;padding:0}
  html,body{width:1200px;height:1006px;overflow:hidden;background:var(--bg-deep)}
  body{font-family:"Mulish",sans-serif;color:var(--ink);position:relative}
  .texture{position:absolute;left:0;width:1200px;
    background:radial-gradient(ellipse at 30% 30%,var(--bg-mid) 0%,#1b1b1b 45%,var(--bg-deep) 100%)}
  .texture--top{top:0;height:402px}
  .texture--bottom{top:537px;height:469px}
  .abs{position:absolute}
  .center{transform:translateX(-50%);text-align:center;white-space:nowrap}

  .main-nav a{display:block;position:absolute;left:222px;transform:translate(-50%,-50%);
    font-size:18px;letter-spacing:2px;color:var(--ink);text-decoration:none;white-space:nowrap}

  .brand{left:600px;top:80px;width:230px;text-align:center;transform:translateX(-50%);font-weight:400}
  .brand__name{font-size:40px;letter-spacing:1px;line-height:44px}
  .brand__rule{height:1px;background:var(--ink);margin:4px 0 6px}
  .brand__sub{font-size:15px;letter-spacing:6px;line-height:18px}
  .address{left:600px;top:176px;font-size:14.5px;line-height:23px;letter-spacing:.4px}

  .secondary-nav a{position:absolute;left:977px;transform:translate(-50%,-50%);
    font-size:14.5px;letter-spacing:.4px;color:var(--ink);text-decoration:none;white-space:nowrap}

  .social{position:absolute;top:260px;width:24px;height:24px;border-radius:50%;background:var(--ink);transform:translateX(-50%)}

  .hours{top:325px;font-size:14.5px;letter-spacing:.5px}
  .hours__day{color:var(--ink-muted);margin-right:10px}
  .hours__time{font-weight:700}

  .mailing{position:absolute;top:402px;left:0;width:1200px;height:135px;background:var(--band)}
  .mailing__title{left:114px;top:43px;font-size:18.5px;font-weight:600;letter-spacing:.6px}
  .mailing__note{left:114px;top:79px;font-size:11px;letter-spacing:.4px;color:var(--ink-soft)}
  .mailing__input{left:562px;top:45px;width:390px;height:44px;background:var(--ink);border:0;
    font-family:inherit;font-size:11px;letter-spacing:.5px;color:#8a8a8a;padding-left:29px;display:flex;align-items:center}
  .mailing__button{left:952px;top:45px;width:133px;height:44px;background:var(--button);
    font-size:11px;font-weight:700;letter-spacing:.6px;display:flex;align-items:center;justify-content:center}

  .section-title{font-size:14.5px;letter-spacing:.5px}
  .partner{font-size:21px;line-height:22px}
  .partner small{display:block;font-size:15px}
  .rating{font-size:21px;font-weight:600;letter-spacing:.3px}
  .stars{display:flex;gap:2px}
  .stars svg{width:19px;height:19px;fill:var(--ink)}
  .review-name{font-size:15px}

  .award{position:absolute}
  .award--dark{background:var(--badge-dark);border:1px solid #444}
  .award--light{background:var(--badge-light);border:1px solid #777}

  .legal{top:975px;font-size:9.5px;letter-spacing:.4px;color:var(--ink-soft)}
  .legal span{margin:0 8px;color:var(--ink-muted)}
</style>
</head>
<body>
  <div class="texture texture--top" role="img" aria-label="Forged carbon fibre texture in black and charcoal"></div>
  <div class="texture texture--bottom" role="img" aria-label="Forged carbon fibre texture in black and charcoal"></div>

  <nav class="main-nav">
    <a href="#" style="top:88px">CURRENT STOCK</a>
    <a href="#" style="top:128px">SELL YOUR CAR</a>
    <a href="#" style="top:168px">PREVIOUSLY SOLD</a>
  </nav>

  <div class="brand abs">
    <div class="brand__name">VELMOR</div>
    <div class="brand__rule"></div>
    <div class="brand__sub">CAR HOUSE</div>
  </div>
  <p class="address abs center">Ashcombe Road, Kelbury,<br>Surrey KB4 2RT</p>

  <nav class="secondary-nav">
    <a href="#" style="top:71px">Delivery &amp; Shipping</a>
    <a href="#" style="top:99px">Privacy Policy</a>
    <a href="#" style="top:127px">Modern Slavery Statement</a>
    <a href="#" style="top:155px">Luxury Cars</a>
    <a href="#" style="top:184px">Contact Us</a>
  </nav>

  <a class="social" href="#" style="left:460px" aria-label="Social profile 1"></a>
  <a class="social" href="#" style="left:527px" aria-label="Social profile 2"></a>
  <a class="social" href="#" style="left:600px" aria-label="Social profile 3"></a>
  <a class="social" href="#" style="left:673px" aria-label="Social profile 4"></a>
  <a class="social" href="#" style="left:748px" aria-label="Social profile 5"></a>

  <p class="hours abs" style="left:245px"><span class="hours__day">MON - FRI</span><span class="hours__time">8:30am - 6:00pm</span></p>
  <p class="hours abs" style="left:517px"><span class="hours__day">SAT</span><span class="hours__time">9:00am - 5:00pm</span></p>
  <p class="hours abs" style="left:745px"><span class="hours__day">SUN</span><span class="hours__time">By Appointment Only</span></p>

  <section class="mailing">
    <h2 class="mailing__title abs">Sign up to Our Mailing List</h2>
    <p class="mailing__note abs">For Event Invitations, Exclusive Previews, Latest Stock and Special Offers.</p>
    <div class="mailing__input abs">Enter Your Email Address</div>
    <div class="mailing__button abs">SUBSCRIBE</div>
  </section>

  <h3 class="section-title abs center" style="left:322px;top:595px">Our Partners</h3>
  <h3 class="section-title abs center" style="left:877px;top:595px">5-stars Reviews</h3>

  <div class="partner abs center" style="left:243px;top:650px">Hartwell<small>Consumer Finance</small></div>
  <div class="partner abs center" style="left:421px;top:650px">Quorin<small>Finance</small></div>

  <div class="rating abs" style="left:627px;top:645px">Excellent</div>
  <div class="stars abs" style="left:749px;top:648px">
    <svg viewBox="0 0 24 24"><path d="M12 2l2.9 6.9 7.1.6-5.4 4.7 1.7 7-6.3-3.8-6.3 3.8 1.7-7L2 9.5l7.1-.6z"/></svg>
    <svg viewBox="0 0 24 24"><path d="M12 2l2.9 6.9 7.1.6-5.4 4.7 1.7 7-6.3-3.8-6.3 3.8 1.7-7L2 9.5l7.1-.6z"/></svg>
    <svg viewBox="0 0 24 24"><path d="M12 2l2.9 6.9 7.1.6-5.4 4.7 1.7 7-6.3-3.8-6.3 3.8 1.7-7L2 9.5l7.1-.6z"/></svg>
    <svg viewBox="0 0 24 24"><path d="M12 2l2.9 6.9 7.1.6-5.4 4.7 1.7 7-6.3-3.8-6.3 3.8 1.7-7L2 9.5l7.1-.6z"/></svg>
    <svg viewBox="0 0 24 24"><path d="M12 2l2.9 6.9 7.1.6-5.4 4.7 1.7 7-6.3-3.8-6.3 3.8 1.7-7L2 9.5l7.1-.6z"/></svg>
  </div>
  <div class="review-name abs center" style="left:803px;top:683px">Ratewell</div>

  <div class="rating abs" style="left:903px;top:645px">Excellent</div>
  <div class="stars abs" style="left:1025px;top:648px">
    <svg viewBox="0 0 24 24"><path d="M12 2l2.9 6.9 7.1.6-5.4 4.7 1.7 7-6.3-3.8-6.3 3.8 1.7-7L2 9.5l7.1-.6z"/></svg>
    <svg viewBox="0 0 24 24"><path d="M12 2l2.9 6.9 7.1.6-5.4 4.7 1.7 7-6.3-3.8-6.3 3.8 1.7-7L2 9.5l7.1-.6z"/></svg>
    <svg viewBox="0 0 24 24"><path d="M12 2l2.9 6.9 7.1.6-5.4 4.7 1.7 7-6.3-3.8-6.3 3.8 1.7-7L2 9.5l7.1-.6z"/></svg>
    <svg viewBox="0 0 24 24"><path d="M12 2l2.9 6.9 7.1.6-5.4 4.7 1.7 7-6.3-3.8-6.3 3.8 1.7-7L2 9.5l7.1-.6z"/></svg>
    <svg viewBox="0 0 24 24"><path d="M12 2l2.9 6.9 7.1.6-5.4 4.7 1.7 7-6.3-3.8-6.3 3.8 1.7-7L2 9.5l7.1-.6z"/></svg>
  </div>
  <div class="review-name abs center" style="left:1077px;top:683px">Praisly</div>

  <h3 class="section-title abs center" style="left:600px;top:758px">Top Awards Acclaimed</h3>
  <div class="award award--dark" style="left:322px;top:812px;width:63px;height:62px" role="img" aria-label="Award badge"></div>
  <div class="award award--light" style="left:432px;top:811px;width:112px;height:61px" role="img" aria-label="Award badge"></div>
  <div class="award award--light" style="left:591px;top:812px;width:71px;height:60px" role="img" aria-label="Award badge"></div>
  <div class="award award--light" style="left:708px;top:811px;width:170px;height:62px" role="img" aria-label="Award badge"></div>

  <p class="legal abs center" style="left:600px">© 2020 Velmor Car House ltd. All rights reserved.<span>|</span>Cookie Policy<span>|</span>Site Map</p>
</body>
</html>
```